Rock Bag Packaging Design

Hey Guys! Hope All is well. I need a designer to make artwork for a cubic foot poly bag. I will packaging rocks into 1 cubic foot bags that measure 18" x 29". The rocks are to be used for drainage, aquaponics, hydroponics, and even decorative ground cover. The rock is very comparable to Brookvale Pebbles and I will be competing against them and other companies like Terramits, Sprou!z, AquaMelt, Pellivar, Fern Baron Clay Pellets, Wetta Puff, just to name a few.
The bags will be clear and color will be printed over it. Need 25%-50% of the bag to be clear to show the rocks. The design can be made to show the rocks in a cool way.
I'm looking for the design to be simple and professional with a earth friendly, green thumb feel.
Information to include on bag...
The product is called 'Pebl Chunx'. This name needs a cool logo.
Reasons to Buy:
-pH Neutral
-Chemically Inert
-Excellent Air to Water Ratio
-Reusable
Uses:
-Decoration
-Drainage
-Hydroponics
-Aquaponics
1 Cu. Ft. (47 LBS)
MADE IN U.S.A.
Updates
Hey All,
Target Market(s)
Hobby/Professional Gardeners
Industry/Entity Type
Product
Requirements
Must have
- Earth Friendly Feel
Feeling that this stuff can grow huge healthy fruits/flowers /root systems

```html
<!DOCTYPE html>
<html lang="en">
<head>
<meta charset="utf-8">
<title>Pebl Chunx – 1 Cu. Ft. Bag Artwork</title>
<link rel="stylesheet" href="https://fonts.googleapis.com/css2?family=Dosis:wght@500;600;700;800&display=swap">
<style>
  :root {
    --leaf: #8cc63f;
    --forest: #1b7a3e;
    --forest-deep: #16692f;
    --mint: #b5dc7e;
    --paper: #ffffff;
    --edge: #d6d6d6;
    --white: #ffffff;
  }
  * { box-sizing: border-box; margin: 0; padding: 0; }
  html, body { width: 777px; height: 1200px; overflow: hidden; background: var(--paper); }
  body { font-family: "Dosis", sans-serif; position: relative; }
  ul { list-style: none; }

  .bag {
    position: absolute; left: 42px; top: 42px; width: 690px; height: 1110px;
    border: 1px solid var(--edge); background: var(--paper); overflow: hidden;
  }

  .benefits {
    position: absolute; left: 0; top: 0; width: 100%; height: 63px; z-index: 3;
    background: var(--forest);
    display: flex; align-items: center; justify-content: space-between;
    padding: 0 18px 0 22px;
  }
  .benefit {
    display: flex; align-items: center; gap: 8px;
    color: var(--white); font-weight: 600; font-size: 21px; line-height: 1;
  }
  .benefit::before {
    content: ""; width: 19px; height: 19px; border-radius: 50%;
    background: var(--white); flex: none;
  }
  .benefit--stacked { color: var(--mint); font-size: 18px; line-height: 0.95; }

  .panel {
    position: absolute; left: 0; top: 63px; width: 100%; height: 720px;
    background: var(--leaf);
  }

  .foliage {
    position: absolute; left: 0; top: 440px; width: 100%; height: 380px;
    background: linear-gradient(180deg, var(--leaf) 0%, var(--forest) 40%, var(--forest-deep) 100%);
  }

  .brand {
    position: absolute; left: 83px; top: 87px; width: 524px; height: 191px; z-index: 2;
    background: var(--forest); border-radius: 16px;
    display: flex; align-items: center; justify-content: center; gap: 26px;
  }
  .brand__dot { width: 40px; height: 40px; border-radius: 50%; background: var(--white); flex: none; }
  .brand__name {
    color: var(--white); font-weight: 800; font-size: 78px; letter-spacing: 2px;
    text-transform: uppercase; line-height: 0.92; white-space: nowrap;
  }
  .brand__line { display: block; }

  .use {
    position: absolute; top: 301px; width: 200px; z-index: 2;
    display: flex; flex-direction: column; align-items: center; gap: 18px;
  }
  .use--decoration { left: 2px; }
  .use--drainage { left: 148px; }
  .use--hydroponics { left: 305px; }
  .use--aquaponics { left: 480px; }
  .use svg { width: 56px; height: 56px; display: block; }
  .use__label { color: var(--forest); font-weight: 600; font-size: 26px; line-height: 1; white-space: nowrap; }

  .spec {
    position: absolute; left: 205px; top: 930px; width: 278px;
    border-radius: 10px; overflow: hidden; text-align: center; font-weight: 700;
  }
  .spec__volume { background: var(--leaf); color: var(--forest); font-size: 27px; padding: 8px 0 6px; }
  .spec__origin { background: var(--forest); color: var(--leaf); font-size: 27px; padding: 10px 0 11px; }
</style>
</head>
<body>
  <main class="bag">
    <ul class="benefits">
      <li class="benefit">pH Neutral</li>
      <li class="benefit">Chemically Inert</li>
      <li class="benefit benefit--stacked">Excellent Air<br>to Water Ratio</li>
      <li class="benefit">Reusable</li>
    </ul>

    <div class="panel"></div>
    <div class="foliage" role="img" aria-label="Silhouettes of lush tropical plants, palms and grasses in dark green"></div>

    <div class="brand">
      <span class="brand__dot"></span>
      <h1 class="brand__name"><span class="brand__line">Pebl</span><span class="brand__line">Chunx</span></h1>
    </div>

    <div class="use use--decoration">
      <svg viewBox="0 0 58 58" aria-hidden="true">
        <circle cx="29" cy="29" r="27" fill="var(--white)"/>
        <path d="M2 26 H56 A27 27 0 0 1 2 26 Z" fill="var(--forest)"/>
      </svg>
      <span class="use__label">Decoration</span>
    </div>
    <div class="use use--drainage">
      <svg viewBox="0 0 58 58" aria-hidden="true">
        <circle cx="29" cy="29" r="27" fill="var(--white)"/>
        <path d="M3 30 H55 A27 27 0 0 1 3 30 Z" fill="var(--forest)"/>
        <g fill="var(--white)">
          <circle cx="13" cy="36" r="3"/><circle cx="21" cy="36" r="3"/><circle cx="29" cy="36" r="3"/><circle cx="37" cy="36" r="3"/><circle cx="45" cy="36" r="3"/>
          <circle cx="17" cy="44" r="3"/><circle cx="25" cy="44" r="3"/><circle cx="33" cy="44" r="3"/><circle cx="41" cy="44" r="3"/>
        </g>
      </svg>
      <span class="use__label">Drainage</span>
    </div>
    <div class="use use--hydroponics">
      <svg viewBox="0 0 58 58" aria-hidden="true">
        <circle cx="29" cy="29" r="27" fill="var(--forest)"/>
        <g fill="none" stroke="var(--white)" stroke-width="3">
          <path d="M6 22 q6 -5 12 0 t12 0 t12 0 t12 0"/>
          <path d="M4 31 q6 -5 12 0 t12 0 t12 0 t12 0"/>
          <path d="M6 40 q6 -5 12 0 t12 0 t12 0 t12 0"/>
        </g>
      </svg>
      <span class="use__label">Hydroponics</span>
    </div>
    <div class="use use--aquaponics">
      <svg viewBox="0 0 58 58" aria-hidden="true">
        <circle cx="29" cy="29" r="27" fill="var(--white)"/>
        <path d="M29 10 C22 22 17 28 17 35 A12 12 0 0 0 41 35 C41 28 36 22 29 10 Z" fill="var(--forest)"/>
      </svg>
      <span class="use__label">Aquaponics</span>
    </div>

    <div class="spec">
      <p class="spec__volume">1 Cu. Ft. (47 LBS)</p>
      <p class="spec__origin">MADE IN U.S.A.</p>
    </div>
  </main>
</body>
</html>
```